Kampfsport Außenwerbung
Zielgruppe
Kampfsportschule für Kinder, Jugendliche und Erwachsene. Sportarten: Kick-Boxen, Jiu-Jitsu und Tricking
Aufgabenstellung
Ich bräuchte für meine Schaufenster eine schöne Außenwerbung. Beworben werden sollen alle meine Sportarten. Ich lade meinen Flyer hoch, damit im ähnlichen Stil gearbeitet werden kann. Außerdem auch noch andere Beispiele an denen man sich orientieren kann, sowie mein Logo und meine Fensterfront.

```html
<!DOCTYPE html>
<html lang="de">
<head>
<meta charset="utf-8">
<title>Martial Arts Murb – Schaufensterwerbung</title>
<link rel="stylesheet" href="https://fonts.googleapis.com/css2?family=Fira+Sans:ital,wght@0,600;0,800;1,800&display=swap">
<style>
  :root {
    --page: #eeeeee;
    --gray: #6e6e70;
    --gray-dark: #4a4a4c;
    --black: #111112;
    --red: #e8412f;
    --orange: #f08468;
    --white: #ffffff;
    --table-bg: #f4f4f4;
    --table-red: #d32a1f;
  }
  * { box-sizing: border-box; margin: 0; padding: 0; }
  html, body { width: 1079px; height: 1200px; overflow: hidden; }
  body { background: var(--page); font-family: "Fira Sans", Arial, sans-serif; position: relative; }

  .storefront { position: absolute; left: 28px; top: 330px; width: 1023px; height: 540px; }

  .pane {
    position: absolute; overflow: hidden;
    background: linear-gradient(135deg,
      var(--gray) 0 28%, var(--black) 28% 52%, var(--red) 52% 53.5%,
      var(--gray) 53.5% 72%, var(--black) 72% 100%);
  }
  .pane--alt {
    background: linear-gradient(135deg,
      var(--black) 0 22%, var(--gray) 22% 46%, var(--orange) 46% 48%,
      var(--black) 48% 70%, var(--red) 70% 72%, var(--gray) 72% 100%);
  }
  .pane--dark {
    background: linear-gradient(135deg,
      var(--gray-dark) 0 18%, var(--black) 18% 60%, var(--red) 60% 62%,
      var(--black) 62% 80%, var(--gray) 80% 100%);
  }
  .band {
    position: absolute; left: 0; right: 0; height: 4px;
    background: linear-gradient(90deg, var(--red), var(--orange));
  }

  /* top row */
  .pane--t1 { left: 1px; top: 17px; width: 134px; height: 114px; }
  .pane--t2 { left: 156px; top: 17px; width: 139px; height: 106px; }
  .pane--header { left: 312px; top: 17px; width: 373px; height: 125px; }
  .pane--t4 { left: 714px; top: 12px; width: 135px; height: 101px; }
  .pane--t5 { left: 868px; top: 2px; width: 146px; height: 112px; }

  /* bottom row */
  .pane--b1 { left: 5px; top: 150px; width: 130px; height: 372px; }
  .pane--b2 { left: 159px; top: 150px; width: 140px; height: 372px; }
  .pane--door-l { left: 333px; top: 165px; width: 152px; height: 354px; }
  .pane--door-r { left: 516px; top: 159px; width: 149px; height: 360px; }
  .pane--b5 { left: 705px; top: 138px; width: 145px; height: 384px; }
  .pane--b6 { left: 868px; top: 133px; width: 146px; height: 392px; }

  .headline { position: absolute; color: var(--white); font-weight: 800; font-style: italic; white-space: nowrap; }
  .headline--main { left: 18px; top: 16px; font-size: 19px; font-style: normal; letter-spacing: .3px; }
  .header-stripe { position: absolute; height: 20px; background: linear-gradient(90deg, var(--red), var(--orange) 70%, transparent); transform: skewX(-25deg); }
  .header-stripe--1 { left: 10px; top: 46px; width: 330px; }
  .header-stripe--2 { left: 0; top: 74px; width: 300px; }
  .headline--sub1 { left: 32px; top: 45px; font-size: 17px; }
  .headline--sub2 { left: 32px; top: 73px; font-size: 17px; }

  .brand {
    position: absolute; display: flex; align-items: center; gap: 5px;
    color: var(--white); font-weight: 800; font-size: 12px; white-space: nowrap;
  }
  .brand__dot { width: 10px; height: 10px; border-radius: 50%; background: var(--red); }
  .brand--t5 { left: 20px; top: 48px; }
  .brand--b2 { left: 14px; top: 52px; }
  .brand--door { left: 28px; top: 120px; font-size: 10px; }

  .photo { position: absolute; }
  .photo--kickboxer { left: 0; top: 150px; width: 265px; height: 220px;
    background: radial-gradient(ellipse at 55% 55%, #c43a4a 0%, #3a1a22 55%, transparent 75%); }
  .photo--bag { left: 88px; top: 90px; width: 40px; height: 110px; background: linear-gradient(90deg, #1c1c1c, #3a3a3a, #1c1c1c); border-radius: 4px; }
  .photo--tricking { left: 20px; top: 80px; width: 115px; height: 270px;
    background: linear-gradient(180deg, #9fc87a 0%, #e8e0d8 30%, #b9c8dc 70%, #d9c6b8 100%); opacity: .85; border-radius: 40px 40px 10px 10px; }
  .photo--jiujitsu { left: 30px; top: 160px; width: 95px; height: 222px;
    background: linear-gradient(180deg, #c9a487 0%, #f3f3f3 25%, #e9e9e9 60%, #e8c437 48%, #f3f3f3 52%, #ececec 100%); border-radius: 30px 30px 6px 6px; }

  .label { position: absolute; color: var(--white); font-weight: 800; font-style: italic; white-space: nowrap; }
  .label--kick { left: 20px; top: 258px; font-size: 22px; line-height: 1; }
  .label--kick span { display: block; font-size: 16px; margin-top: 3px; }
  .label--tricking { left: 8px; top: 270px; font-size: 18px; transform: rotate(-40deg); transform-origin: left bottom; }
  .label--jiu { left: 10px; top: 96px; font-size: 18px; transform: rotate(-35deg); transform-origin: left bottom; }
  .label--selbst { left: 18px; top: 118px; font-size: 13px; font-style: normal; font-weight: 600; transform: rotate(-35deg); transform-origin: left bottom; }

  .contact { position: absolute; left: 20px; top: 272px; color: var(--white); transform: rotate(-35deg); transform-origin: left bottom; white-space: nowrap; }
  .contact__phone { font-size: 14px; font-weight: 800; display: flex; align-items: center; gap: 4px; }
  .contact__mail { font-size: 9px; font-weight: 600; margin-top: 6px; }

  .schedule { position: absolute; left: 4px; top: 84px; width: 138px; padding: 3px; background: var(--table-bg); border-radius: 4px; border-collapse: separate; border-spacing: 1px; font-size: 3.6px; line-height: 1.15; text-align: center; }
  .schedule th { color: var(--black); font-weight: 800; padding: 1px 0; }
  .schedule td { background: #2a2a2a; color: var(--white); padding: 1px 0; }
  .schedule td.is-red { background: var(--table-red); }
  .schedule td.is-empty { background: #ffffff; }
  .schedule td.time { background: var(--table-red); font-weight: 800; }
</style>
</head>
<body>
<div class="storefront">

  <div class="pane pane--t1"><div class="band" style="top:70px"></div></div>
  <div class="pane pane--alt pane--t2"><div class="band" style="top:86px"></div></div>

  <div class="pane pane--dark pane--header">
    <div class="header-stripe header-stripe--1"></div>
    <div class="header-stripe header-stripe--2"></div>
    <div class="headline headline--main">WIR MACHEN KINDER STARK</div>
    <div class="headline headline--sub1">KAMPSPORT &amp;</div>
    <div class="headline headline--sub2">SELBSTVERTEITIGUNG</div>
  </div>

  <div class="pane pane--alt pane--t4"><div class="band" style="top:36px"></div></div>
  <div class="pane pane--dark pane--t5">
    <div class="brand brand--t5"><span class="brand__dot"></span>Martial Arts Murb</div>
  </div>

  <div class="pane pane--b1">
    <div class="band" style="top:78px"></div>
    <div class="photo photo--kickboxer" role="img" aria-label="Foto: Kind in Kickbox-Ausrüstung beim hohen Tritt"></div>
    <div class="label label--kick">KICK<span>BOXEN</span></div>
  </div>
  <div class="pane pane--alt pane--b2">
    <div class="brand brand--b2"><span class="brand__dot"></span>Martial Arts Murb</div>
    <div class="photo photo--bag" role="img" aria-label="Foto: Boxsack"></div>
    <div class="band" style="top:300px"></div>
  </div>

  <div class="pane pane--door-l">
    <div class="band" style="top:286px"></div>
    <div class="photo photo--tricking" role="img" aria-label="Foto: Kind beim Dehnen mit gestrecktem Bein und Gummiband"></div>
    <div class="label label--tricking">TRICKING</div>
  </div>
  <div class="pane pane--dark pane--door-r">
    <div class="band" style="top:292px"></div>
    <div class="brand brand--door"><span class="brand__dot"></span>Martial Arts Murb</div>
    <div class="contact">
      <div class="contact__phone">0152 / 38 60 27 14</div>
      <div class="contact__mail">info@martial-arts-murb.de</div>
    </div>
  </div>

  <div class="pane pane--dark pane--b5">
    <div class="label label--jiu">JIU JITSU</div>
    <div class="label label--selbst">Selbstverteitigung</div>
    <div class="photo photo--jiujitsu" role="img" aria-label="Foto: Kind im weißen Gi mit gelbem Gürtel in Kampfhaltung"></div>
  </div>

  <div class="pane pane--alt pane--b6">
    <div class="band" style="top:260px"></div>
    <div class="band" style="top:300px"></div>
    <table class="schedule">
      <tr><th>Zeit</th><th>MONTAG</th><th>DIENSTAG</th><th>MITTWOCH</th><th>DONNERSTAG</th><th>FREITAG</th></tr>
      <tr><td class="time">15:00</td><td>Kick 3-5</td><td class="is-red">Jitsu 3-6</td><td>Kick 3-5</td><td class="is-red">Jitsu 3-6</td><td class="is-empty"></td></tr>
      <tr><td class="time">16:00</td><td>Kick 6-7</td><td class="is-red">Jitsu 7-12</td><td>Kick 6-7</td><td class="is-red">Jitsu 7-12</td><td>Kick 3-5</td></tr>
      <tr><td class="time">17:00</td><td>Kick 8-10</td><td>Tricking 6+</td><td>Kick 8-10</td><td>Tricking 6+</td><td>Kick 7+</td></tr>
      <tr><td class="time">18:15</td><td>Kick 10-12</td><td>U25</td><td>Kick 10-12</td><td>U25</td><td class="is-empty"></td></tr>
      <tr><td class="time">19:30</td><td>Kick 13+</td><td class="is-empty"></td><td>Kick 13+</td><td class="is-empty"></td><td class="is-empty"></td></tr>
    </table>
  </div>

</div>
</body>
</html>
```